Flyer/Poster design required for volunteer activities

We need a STRIKING A4 Poster/Flyer advertising our conservation volunteer program activities which are currently happening in the area. This poster is to advertise the program once people have arrived on the island or to locals. The program covers 5 months, May-September 2019 and is focused on conservation. I have attached the following:
- a flyer which was previously created (Tidewatch Habitat Helpers 2019 sm)to advertise the program - would prefer it has a similar striking resemblance, but not essential
- A mock up document 'TWHH On Island Poster_2019_v2' with text -Logos-Images

Target Market(s)

Everyone interested in Environmental Adventure/Hiking/Citizen Science

Industry/Entity Type

Tourism

Font styles to use
Sans Serif

Requirements
Must have
• -A travel conservation focus
• -Must use 'TWI-Background Image' as the background to the design
• -The info of where to get more information and the social media details must be prominent

```html
<!DOCTYPE html>
<html lang="en">
<head>
<meta charset="utf-8">
<title>Tidewatch Habitat Helpers – Program 2019</title>
<link rel="stylesheet" href="https://fonts.googleapis.com/css2?family=Oswald:wght@500;600;700&family=Lobster&family=Open+Sans:wght@700;800&display=swap">
<style>
:root{
  --navy:#1f4fa3;
  --ink:#23469a;
  --yellow:#fde124;
  --sky:#dcecf8;
  --sea:#1a82c8;
  --deep:#0f5aa8;
  --white:#ffffff;
}
*{margin:0;padding:0;box-sizing:border-box}
html,body{width:878px;height:1200px;overflow:hidden;background:#e9eef3}
.poster{position:relative;width:878px;height:1200px;overflow:hidden;font-family:"Open Sans",Arial,sans-serif}
.backdrop{position:absolute;inset:0;background:
  linear-gradient(180deg,#eef6fc 0%,#d5e9f7 22%,#8fbcd8 30%,#5d8fb0 36%,#3b9ad3 46%,#2f8ccd 62%,#1d75bf 80%,#0f5aa8 100%)}
.frame{position:absolute;left:19px;top:19px;right:19px;bottom:19px;border:7px solid var(--yellow)}
.header-wash{position:absolute;left:26px;top:26px;right:26px;height:230px;background:linear-gradient(180deg,rgba(255,255,255,.85),rgba(255,255,255,.35))}
.title{position:absolute;left:54px;top:34px;width:600px;white-space:nowrap;font-family:"Oswald",sans-serif;font-weight:700;color:var(--navy);font-size:80px;line-height:1;letter-spacing:1px}
.subtitle{position:absolute;left:56px;top:120px;width:600px;white-space:nowrap;font-family:"Oswald",sans-serif;font-weight:600;color:var(--navy);font-size:34px;letter-spacing:17px;line-height:1}
.badge{position:absolute;left:673px;top:50px;width:140px;height:140px;border-radius:50%;border:4px solid var(--navy);background:var(--white);display:flex;align-items:center;justify-content:center;font-family:"Oswald",sans-serif;font-weight:700;font-size:34px;color:var(--navy)}
.tagline{position:absolute;left:26px;top:172px;width:384px;height:28px;background:var(--yellow);font-family:"Oswald",sans-serif;font-weight:600;color:var(--navy);font-size:15px;letter-spacing:3px;line-height:28px;padding-left:22px}
.dates{position:absolute;left:38px;top:218px;font-family:"Oswald",sans-serif;font-weight:600;color:var(--navy);font-size:25px;line-height:30px}
.join-band{position:absolute;left:302px;top:215px;width:550px;height:29px;background:var(--yellow);font-family:"Oswald",sans-serif;font-weight:600;color:var(--navy);font-size:15px;letter-spacing:3px;line-height:29px;text-align:center}
.feature{position:absolute;width:250px}
.feature .photo{position:absolute;left:37px;top:0;width:176px;height:176px;border-radius:50%;border:5px solid var(--yellow)}
.feature .month{position:absolute;left:75px;top:144px;width:100px;height:20px;background:var(--yellow);font-family:"Oswald",sans-serif;font-weight:600;font-size:14px;color:#1b2d55;text-align:center;line-height:20px}
.feature .week{position:absolute;left:0;top:164px;width:250px;height:20px;background:var(--yellow);font-family:"Oswald",sans-serif;font-weight:600;font-size:14px;color:#1b2d55;text-align:center;line-height:20px}
.feature h2{position:absolute;left:0;top:192px;width:250px;font-family:"Lobster",cursive;font-weight:400;font-size:25px;line-height:28px;color:var(--white);text-align:center;-webkit-text-stroke:1px var(--navy);text-shadow:2px 2px 0 var(--navy)}
.feature ul{position:absolute;left:10px;top:268px;width:235px;list-style:none}
.feature li{position:relative;padding-left:18px;margin-bottom:10px;font-size:12.5px;line-height:14px;font-weight:700;color:var(--ink);text-shadow:0 0 3px rgba(255,255,255,.9)}
.feature li::before{content:"";position:absolute;left:0;top:4px;width:6px;height:6px;border-radius:50%;background:var(--yellow)}
.f-may{left:41px;top:277px}
.f-jun{left:312px;top:277px}
.f-jul{left:585px;top:277px}
.f-aug{left:41px;top:735px}
.f-sep{left:330px;top:735px}
.f-sep ul{top:228px;width:210px}
.info{position:absolute;left:600px;top:722px;width:230px;height:250px}
.info .quote{position:absolute;width:30px;height:44px}
.info .q-open{left:15px;top:0}
.info .q-close{left:162px;top:190px}
.info p{position:absolute;left:0;top:14px;width:230px;font-family:"Lobster",cursive;font-size:19px;line-height:24px;color:var(--white);text-align:center;-webkit-text-stroke:.6px var(--navy);text-shadow:1.5px 1.5px 0 var(--navy)}
.follow{position:absolute;left:596px;top:1006px;width:224px;height:160px;background:#fdf3cc;border:3px solid var(--yellow);padding:22px 12px 0 14px}
.follow h3{font-family:"Oswald",sans-serif;font-weight:600;font-size:24px;color:var(--navy);text-align:center;letter-spacing:.5px}
.follow .handle{display:flex;align-items:center;gap:8px;margin-top:14px;font-family:"Oswald",sans-serif;font-weight:600;font-size:12px;color:var(--navy);white-space:nowrap}
.follow .dot{width:18px;height:18px;border-radius:50%;border:2px solid var(--navy);flex:none}
</style>
</head>
<body>
<main class="poster">
  <div class="backdrop" role="img" aria-label="Background photograph of the island's peaks and turquoise lagoon under a pale sky"></div>
  <div class="header-wash"></div>
  <div class="frame"></div>

  <h1 class="title">TIDEWATCH ISLE</h1>
  <div class="subtitle">HABITAT HELPERS</div>
  <div class="badge">TWHH</div>
  <div class="tagline">BE INVOLVED IN PROTECTING PARADISE</div>
  <div class="dates">• MAY – SEPTEMBER 2019 •</div>
  <div class="join-band">JOIN THE TIDEWATCH HABITAT HELPERS PROGRAM 2019</div>

  <section class="feature f-may">
    <div class="photo" role="img" aria-label="Photo of a grey seabird resting among green plants" style="background:radial-gradient(circle at 45% 40%,#a89a8a,#5c6a3a 70%,#3b4d2a)"></div>
    <div class="week">FEATURE WEEK: 19TH – 26TH MAY</div>
    <div class="month">MAY 2019</div>
    <h2>Birds Of Tidewatch<br>Isle</h2>
    <ul>
      <li>Ocean bird watching boat trips</li>
      <li>Guided tours of Woodhen and Currawong quarters</li>
      <li>Weekly lectures at the Tidewatch Isle Museum</li>
      <li>Weekly screenings of documentaries on Bird and Island Conservation projects</li>
      <li>Self guided land bird survey</li>
    </ul>
  </section>

  <section class="feature f-jun">
    <div class="photo" role="img" aria-label="Photo of a snorkeller recording notes underwater" style="background:radial-gradient(circle at 50% 60%,#2a4a6a,#1e8fd0 60%,#3fb4e6)"></div>
    <div class="week">FEATURE WEEK: 3RD- 9TH JUNE</div>
    <div class="month">JUNE 2019</div>
    <h2>Tidewatch Isle<br>Marine Park</h2>
    <ul>
      <li>Marine pest monitoring with marine park staff</li>
      <li>Marine plastic &amp; debris clean up activities</li>
      <li>Screenings of marine conservation documentaries at the museum</li>
      <li>Weekly lectures on Marine Life at the Tidewatch Isle Museum</li>
      <li>Marine Activities with local operators</li>
    </ul>
  </section>

  <section class="feature f-jul">
    <div class="photo" role="img" aria-label="Photo of a hiker walking through palm forest" style="background:radial-gradient(circle at 50% 50%,#c9b06a,#6f7a2e 55%,#3a4a1e)"></div>
    <div class="week">FEATURE WEEK: 21ST – 28TH JULY</div>
    <div class="month">JULY 2019</div>
    <h2>Invasive Species</h2>
    <ul style="top:236px">
      <li>Guided walks to learn about the weed eradication program</li>
      <li>Weekly lectures on plants of Tidewatch Isle</li>
      <li>Weekly screenings of documentaries on plant and island conservation projects</li>
      <li>Guided walks to Mount Harrow</li>
      <li>Local tour guides include commentaries on island plants</li>
    </ul>
  </section>

  <section class="feature f-aug">
    <div class="photo" role="img" aria-label="Photo of a large dark stick insect held in two hands" style="background:radial-gradient(circle at 50% 50%,#e4c2b0,#c79a86 60%,#a6c2d4)"></div>
    <div class="week">FEATURE WEEK: 11TH-19TH AUGUST</div>
    <div class="month">AUGUST 2019</div>
    <h2>Amazing<br>Invertebrates</h2>
    <ul>
      <li>Guided night walks to learn about the island's invertebrates</li>
      <li>Weekly viewing and presentation of the Tidewatch Isle Phasmid</li>
      <li>Weekly lectures on invertebrates of Tidewatch Isle at the museum</li>
      <li>Weekly screenings of documentaries on island conservation projects</li>
    </ul>
  </section>

  <section class="feature f-sep">
    <div class="photo" role="img" aria-label="Photo of a walker on a grassy headland above the sea" style="background:linear-gradient(180deg,#cfe3f2 0%,#9cc3e0 45%,#3a86b8 60%,#5d7a3a 80%,#3e5a26)"></div>
    <div class="week">FEATURE WEEK: 1ST-8TH SEPTEMBER</div>
    <div class="month">SEPTEMBER 2019</div>
    <h2>Protecting Paradise</h2>
    <ul>
      <li>Observational snorkel surveys with Marine Ecologists, to assess populations of McCulloch's Anemonefish and other unique fish species</li>
      <li>Guided snorkel and glass bottom boat tour to assess coral health within the Tidewatch Isle Marine Park</li>
      <li>Guided walks to learn about the island's conservation history</li>
    </ul>
  </section>

  <aside class="info">
    <svg class="quote q-open" viewBox="0 0 30 44"><path d="M15 0a15 15 0 1 1 0 30c2 6 -2 12 -8 14c4-5 5-9 4-14A15 15 0 0 1 15 0z" fill="var(--yellow)"/></svg>
    <p>See the<br><br>TWI visitor centre for more information about the Tidewatch Habitat Helpers program<br><br>for 2019</p>
    <svg class="quote q-close" viewBox="0 0 30 44"><path d="M15 0a15 15 0 1 1 0 30c2 6 -2 12 -8 14c4-5 5-9 4-14A15 15 0 0 1 15 0z" fill="var(--yellow)"/></svg>
  </aside>

  <aside class="follow">
    <h3>FOLLOW US!</h3>
    <div class="handle"><span class="dot"></span>FRIENDSPACE.EXAMPLE/TWHH</div>
    <div class="handle"><span class="dot"></span>SNAPGRAM@TWHH</div>
  </aside>
</main>
</body>
</html>
```